Velora Lounge Duo Flyer - info and save 20%

We need a flyer designed around the look of our website - that retro feel - it can give some brief info on our duo and we need to present an offer of 20% off our normal prices for live music at private or corporate events and weddings.
Two hours $590 Now $472
Three hours $690 Now $ 552
Four hours $790 Now $632
Five hours $890 Now $712
About our duo:
Velora Duo - Live Jazz and Cocktail Music
Set the atmosphere with classy cocktail music and jazz at your next event of distinction. Marnie Holt on Piano and Gavin Thorley on the Bass - professional and dedicated musicians. All venues and all occasions. Servicing Brisbane & South-East Queensland. Acoustic or Electric - all venue sizes.
Testimonials:
Sat. March 21, 2013 | Fendrix Awards Dinner at the Palmvale Arts Centre
The Velora Duo provided the perfect entertainment for our Awards Dinner. It was fantastic to have the combination of purely background music and more upbeat music with vocals. Marnie was brilliant to deal with from the initial booking stage to the event and ensured that the entertainment option provided was the most suitable for our event.
Dana Whitcombe, Fendrix Pty Ltd
_______________________________________________________________________
Sat. June 26, 2012 | Wedding at the Riverbend Hall of Qld
We had Velora Duo play at our Cocktail Wedding Reception for the first couple of hours and they were simply delightful! The music was diverse, fun and great way to create a buzzing atmosphere while still having your guests being able to enjoy their conversations. As everyone knows weddings can be stressful but it was such a pleasure was dealing with Marnie Holt (pianist) of Velora Duo as she was completely helpful and professional in organising the music list and the arrangement and put our minds at rest knowing we were dealing with such professional and experienced musicians. It was a wonderful start to the evening and we had many complements on the wonderful music from our guests! It again completely reaffirmed to us how important good music is for creating a memorable experience on your wedding day and we cannot recommend Velora Duo and their pianist Marnie Holt enough!
Tessa & Martin, June 2012,
Fri. April 21st, 2011 | Surprise Birthday Party – Kestrel Club
You simply made the evening with your music. Thank you Velora Duo for another great night!”
Doyle Family 2011,
Fri. October 1st, 2010 - ongoing | Harbourview Manor, Queensland
It has been an absolute pleasure to have Marnie & Gavin perform for us at Harbourview Manor. Their love and passion for music is brought to life through their flawless performances and never cease to amaze myself or our guests with what they will come up with next. Marnie and Gavin are such wonderful characters who are willing to go above and beyond to support Harbourview Manor with whatever musical requests and repertoire we require.
Marnie has also been a fantastic help to me with the recommendation of other Brisbane based musicians whose professionalism and commitment to the music industry is faultless.
I would like to thank Marnie and Gavin and the Tidewave Sound team for their continuing musical support to Harbourview Manor.
Colleen Ashby - Assistant House Manager - Harbourview Manor Queensland
Updates
This project was meant to finish today - 25 Aug - I am not sure why it is saying that it has 7 more days to run - but we need it by tomorrow really !! (26 Aug)
This is a message from the printers re the design specs!
Design files> PDF settings. All CMYK colour settings no RGB.
Print ready files to have the noted minimum 3mm bleed design and the noted crop marks for final trim size.
1 up front, 1 up backs for cards or leaflets etc.

```html
<!DOCTYPE html>
<html lang="en">
<head>
<meta charset="utf-8">
<title>Velora Duo – Trifold Brochure</title>
<link rel="stylesheet" href="https://fonts.googleapis.com/css2?family=Josefin+Sans:wght@400;600&family=Oswald:wght@400;500&family=Source+Code+Pro:ital,wght@0,400;0,600;1,600&display=swap">
<style>
:root{
  --backdrop:#3b3b3b;
  --teal:#7db2b4;
  --cream:#f3ebd2;
  --ink:#3a3a3a;
  --paper:#e3e5e5;
  --orange:#d8663d;
  --orange-dark:#b8532f;
  --date-box:#3d3d3d;
  --flap:#2f2f2f;
  --photo-warm:#6b4428;
  --photo-deep:#2e1d12;
}
*{box-sizing:border-box;margin:0;padding:0}
html,body{width:1200px;height:874px;overflow:hidden}
body{background:var(--backdrop);position:relative;font-family:"Source Code Pro",monospace;color:var(--ink)}

/* ---------- Cover panel ---------- */
.cover{position:absolute;left:14px;top:90px;width:236px;height:694px;background:var(--teal);overflow:hidden}
.cover-title{font-family:"Josefin Sans",sans-serif;font-weight:400;font-size:31px;letter-spacing:1.5px;color:var(--cream);text-align:center;margin-top:30px;white-space:nowrap}
.cover-ribbon{display:block;margin:8px auto 0;width:204px;height:30px}
.cover-photo{position:absolute;left:0;top:116px;width:236px;height:196px;background:linear-gradient(160deg,var(--photo-warm) 0%,#9a6a3e 45%,var(--photo-deep) 100%)}
.cover-art{position:absolute;right:0;top:290px;width:130px;height:404px;background:linear-gradient(180deg,rgba(243,235,210,.15),rgba(243,235,210,.85) 55%,var(--cream))}
.musician{position:absolute;left:18px;font-family:"Oswald",sans-serif;color:var(--ink)}
.musician-name{font-size:18px;font-weight:500;font-style:italic;letter-spacing:.4px;white-space:nowrap}
.musician-role{display:flex;align-items:center;gap:6px;font-size:9px;letter-spacing:2px;margin-top:2px}
.musician-role::before,.musician-role::after{content:"";height:1px;width:40px;background:var(--ink)}
.musician.piano{top:360px}
.musician.bass{top:424px}

/* ---------- Offer flap ---------- */
.offer{position:absolute;left:256px;top:90px;width:236px;height:694px;background:var(--flap);color:var(--cream);padding:28px 20px}
.offer-heading{font-family:"Oswald",sans-serif;font-weight:500;font-size:16px;letter-spacing:1px;color:var(--teal)}
.offer-about{font-size:9.6px;line-height:13.6px;margin-top:10px;color:#dcdcd6}
.offer-rule{height:6px;margin:22px 0;background:repeating-linear-gradient(135deg,var(--orange) 0 1.5px,transparent 1.5px 5px);opacity:.8}
.offer-save{font-family:"Josefin Sans",sans-serif;font-weight:600;font-size:44px;line-height:1;color:var(--orange);letter-spacing:1px}
.offer-events{font-family:"Oswald",sans-serif;font-size:15px;line-height:20px;letter-spacing:1.5px;margin-top:10px;color:var(--cream)}
.price-list{width:100%;border-collapse:collapse;margin-top:20px;font-size:10px}
.price-list th{font-family:"Oswald",sans-serif;font-weight:400;font-size:10px;letter-spacing:1px;color:var(--teal);text-align:left;padding-bottom:6px;border-bottom:1px solid #555}
.price-list td{padding:7px 0;border-bottom:1px dashed #555}
.price-list .was{color:#999;text-decoration:line-through}
.price-list .now{color:var(--orange);font-weight:600}
.price-list .num{text-align:right}
.offer-note{font-size:9px;line-height:13px;color:#aaa;margin-top:16px}

/* ---------- Inside spread ---------- */
.spread{position:absolute;left:498px;top:90px;width:690px;height:694px;background:var(--paper);display:flex}
.panel{width:230px;height:100%;padding:24px 18px;position:relative;border-right:1px solid #d2d5d5}
.panel:last-child{border-right:none}

.entry{margin-bottom:22px}
.entry-head{display:flex;gap:9px;align-items:flex-start;margin-bottom:11px}
.date{width:38px;background:var(--date-box);color:#eee;text-align:center;font-family:"Oswald",sans-serif;flex:none}
.date-day{font-size:16px;line-height:23px}
.date-month{font-size:9.5px;letter-spacing:1px;line-height:15px;border-top:1px solid #777}
.event{font-family:"Oswald",sans-serif;font-size:11px;line-height:15px;color:var(--ink);padding-top:2px}
.entry-body{font-size:9.6px;line-height:13.6px}
.entry-body p+p{margin-top:6px}
.signature{font-weight:600;font-style:italic;color:var(--orange);font-size:9.6px;line-height:13.6px;margin-top:6px}

.dash-rule{height:0;border-top:2px dashed var(--orange);opacity:.55;margin:0 0 22px}
.panel-art{position:absolute;left:30px;bottom:0;width:110px;height:110px;background:radial-gradient(circle at 50% 70%,rgba(150,150,150,.25),rgba(150,150,150,0) 70%)}

.web-ribbon{display:block;width:194px;height:36px;margin-bottom:20px}
.spread-title{font-family:"Josefin Sans",sans-serif;font-weight:600;font-size:29px;letter-spacing:1px;color:var(--orange);white-space:nowrap}
.stripe-rule{height:6px;margin:4px 0 18px;background:repeating-linear-gradient(135deg,var(--orange) 0 1.5px,transparent 1.5px 5px);opacity:.7}
</style>
</head>
<body>

<section class="cover" aria-label="Brochure cover">
  <h1 class="cover-title">VELORA DUO</h1>
  <svg class="cover-ribbon" viewBox="0 0 204 30" aria-label="Classic cocktail music">
    <polygon points="0,5 16,5 10,15 16,25 0,25 7,15" fill="#d9d0b3"/>
    <polygon points="204,5 188,5 194,15 188,25 204,25 197,15" fill="#d9d0b3"/>
    <rect x="12" y="2" width="180" height="26" fill="var(--cream)"/>
    <text x="102" y="20" text-anchor="middle" font-family="Oswald, sans-serif" font-size="12" letter-spacing="1.2" fill="var(--ink)">CLASSIC COCKTAIL MUSIC</text>
  </svg>
  <div class="cover-photo" role="img" aria-label="Photo of the duo performing on grand piano and double bass in a warm wood-panelled room"></div>
  <div class="cover-art" role="img" aria-label="Illustration of a double bass merged with piano keys in cream"></div>
  <div class="musician piano">
    <div class="musician-name">MARNIE HOLT</div>
    <div class="musician-role">PIANO</div>
  </div>
  <div class="musician bass">
    <div class="musician-name">GAVIN THORLEY</div>
    <div class="musician-role">BASS</div>
  </div>
</section>

<section class="offer" aria-label="About the duo and special offer">
  <h2 class="offer-heading">LIVE JAZZ &amp; COCKTAIL MUSIC</h2>
  <p class="offer-about">Set the atmosphere with classy cocktail music and jazz at your next event of distinction. Marnie Holt on Piano and Gavin Thorley on the Bass - professional and dedicated musicians. All venues and all occasions. Servicing Brisbane &amp; South-East Queensland. Acoustic or Electric - all venue sizes.</p>
  <div class="offer-rule"></div>
  <div class="offer-save">SAVE 20%</div>
  <div class="offer-events">PRIVATE &amp; CORPORATE<br>EVENTS &amp; WEDDINGS</div>
  <table class="price-list">
    <thead><tr><th>LIVE MUSIC</th><th class="num">WAS</th><th class="num">NOW</th></tr></thead>
    <tbody>
      <tr><td>Two hours</td><td class="num was">$590</td><td class="num now">$472</td></tr>
      <tr><td>Three hours</td><td class="num was">$690</td><td class="num now">$552</td></tr>
      <tr><td>Four hours</td><td class="num was">$790</td><td class="num now">$632</td></tr>
      <tr><td>Five hours</td><td class="num was">$890</td><td class="num now">$712</td></tr>
    </tbody>
  </table>
  <p class="offer-note">20% off our normal prices for live music.</p>
</section>

<section class="spread" aria-label="Brochure inside spread">
  <div class="panel">
    <article class="entry">
      <div class="entry-head">
        <div class="date"><div class="date-day">21</div><div class="date-month">MAR</div></div>
        <div class="event">Awards Dinner<br>Palmvale Arts Centre</div>
      </div>
      <div class="entry-body">
        <p>The Velora Duo provided the perfect entertainment for our Awards Dinner. It was fantastic to have the combination of purely background music and more upbeat music with vocals. Marnie was brilliant to deal with from the initial booking stage to the event and ensured that the entertainment option provided was the most suitable for our event.</p>
      </div>
      <div class="signature">Dana Whitcombe, Fendrix Pty Ltd, 2013</div>
    </article>
    <div class="dash-rule"></div>
    <article class="entry">
      <div class="entry-head">
        <div class="date"><div class="date-day">21</div><div class="date-month">APR</div></div>
        <div class="event">Surprise Birthday Party<br>Kestrel Club</div>
      </div>
      <div class="entry-body">
        <p>You simply made the evening with your music. Thank you Velora Duo for another great night!</p>
      </div>
      <div class="signature">Doyle Family, 2011</div>
    </article>
    <div class="panel-art" role="img" aria-label="Faint illustration of a double bass with piano keys"></div>
  </div>

  <div class="panel">
    <svg class="web-ribbon" viewBox="0 0 194 36" aria-label="www.veloraloungeduo.com">
      <line x1="0" y1="18" x2="194" y2="18" stroke="var(--orange)" stroke-width="1.5" stroke-dasharray="4 3" opacity=".6"/>
      <polygon points="4,7 19,7 14,18 19,29 4,29 10,18" fill="var(--orange-dark)"/>
      <polygon points="190,7 175,7 180,18 175,29 190,29 184,18" fill="var(--orange-dark)"/>
      <rect x="15" y="4" width="164" height="28" fill="var(--orange)"/>
      <text x="97" y="22.5" text-anchor="middle" font-family="Oswald, sans-serif" font-size="11.5" letter-spacing=".8" fill="var(--ink)">WWW.VELORALOUNGEDUO.COM</text>
    </svg>
    <article class="entry">
      <div class="entry-head">
        <div class="date"><div class="date-day">26</div><div class="date-month">JUN</div></div>
        <div class="event">Wedding<br>Riverbend Hall of Qld</div>
      </div>
      <div class="entry-body">
        <p>We had Velora Duo play at our Cocktail Wedding Reception for the first couple of hours and they were simply delightful! The music was diverse, fun and great way to create a buzzing atmosphere while still having your guests being able to enjoy their conversations. As everyone knows weddings can be stressful but it was such a pleasure was dealing with Marnie Holt (pianist) of Velora Duo as she was completely helpful and professional in organising the music list and the arrangement and put our minds at rest knowing we were dealing with such professional and experienced musicians. It was a wonderful start to the evening and we had many complements on the wonderful music from our guests! It again completely reaffirmed to us how important good music is for creating a memorable experience on your wedding day and we cannot recommend Velora Duo and their pianist Marnie Holt enough!</p>
      </div>
      <div class="signature">Tessa &amp; Martin, 2012</div>
    </article>
  </div>

  <div class="panel">
    <h2 class="spread-title">VELORA DUO</h2>
    <div class="stripe-rule"></div>
    <article class="entry">
      <div class="entry-head">
        <div class="date"><div class="date-day">1</div><div class="date-month">OCT</div></div>
        <div class="event">Ongoing<br>Harbourview Manor, Queensland</div>
      </div>
      <div class="entry-body">
        <p>It has been an absolute pleasure to have Marnie &amp; Gavin perform for us at Harbourview Manor. Their love and passion for music is brought to life through their flawless performances and never cease to amaze myself or our guests with what they will come up with next. Marnie and Gavin are such wonderful characters who are willing to go above and beyond to support Harbourview Manor with whatever musical requests and repertoire we require.</p>
        <p>Marnie has also been a fantastic help to me with the recommendation of other Brisbane based musicians whose professionalism and commitment to the music industry is faultless.</p>
        <p>I would like to thank Marnie and Gavin and the Tidewave Sound team for their continuing musical support to Harbourview Manor.</p>
      </div>
      <div class="signature">Colleen Ashby - Assistant House Manager - Harbourview Manor Queensland, 2010</div>
    </article>
  </div>
</section>

</body>
</html>
```